Tollard Cove Marina Website

Business Background
Tollard Cove Marine is a full-service marina situated in Moriches Bay just two miles west of Moriches Inlet. Our 2 1/2 acres of waterfront real estate includes over 50 wet slips, jetski ports and dry storage that can accommodate boats as small as 13′ to boats up to 50′ in length. Our boaters are offered a safe, secure and family friendly environment while our staff is able to provide almost any service you could need for your boat to include shrink wrapping, bottom painting, detailing, mechanical repairs, new/used boat sales and much much more.

Would like a tab for the following:

Marina (summer dockage & winter storage)
Under marina tab list the following
FEATURES
All of our floating docks offer dockside electric, and water.
Summer Dockage
Need a place to keep your boat?
Winter & Summer Storage
Need a place to stay? We offer full transient dockage.
Transient Dockage
With easy access from the Pellow Creek
On site mechanical services provided.
Mechanical Services
Don't worry if you're forgetting something. We offer a full range of boating necessities.
Bait, Ice & Ship Store
Both long, and short haul services are available.
35 ton Open-End Travel Lift & Forklift
Our marina offers an keyfob access electronic gate, as well as video surveillance.
Security
Member only restroom, and shower.
Full Bathroom Facilities
Just minutes from Great Gun & Moriches Inlet
Ideal Fishermen Location
On site charters

Harborline Assist
Outboard Repairs & Repowers (using ferrow & kesta)
New Boat sales
Used Boat sales
Contact us

Link on home page to Facebook and Instagram
live weather link and noaa link

Industry/Entity Type

Marina

Coding

Coded - Design and coding required

Number of Pages Required

1 page

Colors
0054AA
0677BA
7BADD7
CADEEF
E8F1F8

Requirements
Must have
• Multiple pages prefer a dark page with blue like my logo

```html
<!DOCTYPE html>
<html lang="en">
<head>
<meta charset="utf-8">
<title>Tollard Cove Marine</title>
<link rel="stylesheet" href="https://fonts.googleapis.com/css2?family=Montserrat:ital,wght@0,400;0,500;0,600;0,700;0,800;1,800;1,900&family=Open+Sans:wght@400;600&display=swap">
<style>
:root{
  --navy:#0f1416;
  --dark:#1b1d1f;
  --ink:#222;
  --muted:#555;
  --blue:#0054aa;
  --blue-mid:#0677ba;
  --blue-light:#7badd7;
  --blue-pale:#cadeef;
  --blue-mist:#e8f1f8;
  --accent:#29a8e0;
  --white:#fff;
}
*{box-sizing:border-box;margin:0;padding:0}
html,body{width:1200px;height:4676px;overflow:hidden;background:var(--white)}
body{position:relative;font-family:"Open Sans",Arial,sans-serif;color:var(--ink)}
.h-display{font-family:"Montserrat",Arial,sans-serif;font-weight:900;font-style:italic;text-transform:uppercase;letter-spacing:1px}
.eyebrow{font-family:"Montserrat",Arial,sans-serif;font-weight:700;font-size:17px;text-transform:uppercase;letter-spacing:.5px}
section{position:absolute;left:0;width:1200px}
.btn{display:inline-block;font-family:"Montserrat",Arial,sans-serif;font-weight:700;font-size:12px;letter-spacing:.5px;text-transform:uppercase;padding:9px 22px;border:2px solid currentColor;text-decoration:none}
.btn-light{background:var(--white);color:var(--ink);border-color:var(--white)}
.btn-outline{color:var(--white);border-color:#bbb}
.btn-outline-dark{color:var(--ink);border-color:#888}
.ph{position:absolute}

/* hero */
.hero{top:0;height:800px;background:linear-gradient(180deg,#163a3e 0%,#1e4f52 40%,#12302f 100%)}
.hero-photo{left:0;top:0;width:1200px;height:800px;background:radial-gradient(ellipse at 30% 40%,#2f6a69 0%,#1a4446 50%,#0f2627 100%)}
.nav{position:absolute;top:22px;left:190px;right:190px;display:flex;align-items:center;justify-content:space-between}
.brand{display:flex;align-items:center;gap:10px;font-family:"Montserrat",Arial,sans-serif;font-weight:800;font-size:18px;color:var(--white);text-transform:uppercase}
.brand-dot{width:34px;height:34px;border-radius:50%;background:var(--blue-mid)}
.nav-links{display:flex;gap:26px;list-style:none;font-family:"Montserrat",Arial,sans-serif;font-size:12px;font-weight:500;color:var(--white)}
.nav-tools{display:flex;gap:14px;align-items:center}
.nav-menu{width:34px;height:34px;border-radius:50%;background:var(--white);display:flex;align-items:center;justify-content:center}
.hero-copy{position:absolute;top:255px;left:0;width:1200px;text-align:center;color:var(--white)}
.hero-copy .eyebrow{font-size:18px}
.hero-copy h1{font-size:58px;line-height:64px;margin-top:8px}
.hero-copy p{width:620px;margin:14px auto 22px;font-size:13px;line-height:19px}
.hero-wave{position:absolute;left:0;bottom:0}

/* about */
.about{top:800px;height:480px}
.about-photo{left:188px;top:100px;width:404px;height:324px;background:linear-gradient(180deg,#9fc4e0 0%,#6a9cc2 45%,#2f6f97 100%)}
.about-copy{position:absolute;left:632px;top:100px;width:380px}
.about-copy .eyebrow{color:var(--blue-mid)}
.about-copy h2{font-size:44px;margin:2px 0 14px}
.about-copy p{font-size:13px;line-height:19px;color:var(--muted)}
.ticks{list-style:none;margin:18px 0 22px;font-size:12px;line-height:17px;color:var(--ink)}
.ticks li{padding-left:18px;position:relative;margin-bottom:10px}
.ticks li:before{content:"";position:absolute;left:2px;top:5px;width:6px;height:6px;border-radius:50%;background:var(--ink)}

/* services */
.services{top:1260px;height:790px;background:var(--dark);color:var(--white)}
.sec-head{text-align:center}
.sec-head h2{font-size:44px;margin-top:4px}
.sec-head p{width:820px;margin:12px auto 0;font-size:12px;line-height:18px}
.card-row{position:absolute;left:188px;width:824px;display:flex;gap:16px}
.svc{width:264px;text-align:center}
.svc-photo{position:relative;height:140px}
.svc h3{font-family:"Montserrat",Arial,sans-serif;font-weight:800;font-style:italic;font-size:18px;text-transform:uppercase;margin:30px 0 10px}
.svc p{font-size:12px;line-height:17px}
.more{display:block;font-family:"Montserrat",Arial,sans-serif;font-weight:700;font-size:11px;color:var(--accent);margin-top:10px;text-decoration:none}

/* products */
.products{top:2050px;height:870px}
.engine{top:60px;width:170px;height:330px;background:linear-gradient(180deg,#f4f5f6 0%,#cfd3d6 60%,#8a9094 100%);border-radius:40px 40px 20px 20px}
.boat-scene{left:0;top:370px;width:1200px;height:500px;background:linear-gradient(180deg,#ffffff 0%,#d9dde0 35%,#8ea0ab 60%,#5d7382 100%)}

/* blogs */
.blogs{top:3010px;height:640px}
.blog-head{position:absolute;left:188px;top:58px;width:620px}
.blog-head .eyebrow{color:var(--blue-mid)}
.blog-head h2{font-size:44px;margin:2px 0 10px}
.blog-head p{font-size:12px;line-height:18px;color:var(--muted)}
.post{width:264px}
.post-photo{position:relative;height:140px}
.post h3{font-family:"Montserrat",Arial,sans-serif;font-weight:800;font-style:italic;font-size:18px;line-height:21px;text-transform:uppercase;margin:28px 0 10px}
.post p{font-size:12px;line-height:17px;color:var(--muted)}

/* testimonials */
.reviews{top:3640px;height:680px;background:var(--dark);color:var(--white)}
.quote{width:264px;height:270px;border:1px solid #4a8fb0;background:#23272a;padding:28px 24px;text-align:center}
.quote p{font-size:12px;line-height:17px;margin:14px 0}
.quote strong{font-family:"Montserrat",Arial,sans-serif;font-size:13px;display:block}
.quote small{font-size:11px;color:#aaa}
.arrow-btn{position:absolute;top:4170px;width:36px;height:36px;border-radius:50%;border:1.5px solid var(--white);display:flex;align-items:center;justify-content:center}

/* footer */
.footer{top:4320px;height:320px}
.foot-col{position:absolute;top:58px}
.foot-col h4{font-family:"Montserrat",Arial,sans-serif;font-weight:800;font-size:16px;text-transform:uppercase;margin-bottom:18px}
.foot-col ul{list-style:none;font-size:12px;line-height:24px;color:var(--muted)}
.foot-col .row{display:flex;gap:10px;align-items:center}
.brand-dark{color:var(--ink)}
.connect{position:absolute;left:784px;top:40px;width:228px;height:210px;background:var(--blue-mist);border:1px solid var(--blue-pale);padding:20px}
.connect h4{font-family:"Montserrat",Arial,sans-serif;font-weight:800;font-size:15px;text-transform:uppercase;margin-bottom:14px}
.field{height:26px;background:var(--white);border:1px solid var(--blue-pale);margin-bottom:10px;font-size:11px;color:#888;padding:5px 8px}
.submit{height:28px;background:var(--blue-mid);color:var(--white);font-family:"Montserrat",Arial,sans-serif;font-weight:700;font-size:11px;text-align:center;line-height:28px}
.copyright{position:absolute;top:4640px;left:0;width:1200px;height:36px;background:var(--dark);color:#ccc;font-size:11px;text-align:center;line-height:36px}
</style>
</head>
<body>

<section class="hero">
  <div class="ph hero-photo" role="img" aria-label="Aerial photo of a boat cutting across dark green water"></div>
  <nav class="nav">
    <div class="brand"><span class="brand-dot"></span>Tollard Cove</div>
    <ul class="nav-links">
      <li>Services</li><li>Summer Storage</li><li>Winter &amp; Summer Storage</li><li>Transient Dockage</li><li>Mechanical Services</li>
    </ul>
    <div class="nav-tools">
      <svg width="18" height="18" viewBox="0 0 18 18"><circle cx="7.5" cy="7.5" r="5.5" fill="none" stroke="#fff" stroke-width="2"/><line x1="11.5" y1="11.5" x2="16" y2="16" stroke="#fff" stroke-width="2"/></svg>
      <div class="nav-menu"><svg width="14" height="12" viewBox="0 0 14 12"><rect y="0" width="14" height="2" fill="#222"/><rect y="5" width="14" height="2" fill="#222"/><rect y="10" width="14" height="2" fill="#222"/></svg></div>
    </div>
  </nav>
  <div class="hero-copy">
    <div class="eyebrow">Tollard Cove Marine</div>
    <h1 class="h-display">Explore the Waters<br>With Confidence</h1>
    <p>A full-service marina with wet slips, jetski ports and dry storage, two miles west of the inlet. Safe, secure and family friendly for every boater on the bay.</p>
    <a class="btn btn-light">Contact Us</a>
  </div>
  <svg class="hero-wave" width="1200" height="180" viewBox="0 0 1200 180"><path d="M0 90 C220 20 420 170 640 120 C860 70 1000 40 1200 110 L1200 180 L0 180Z" fill="#fff"/></svg>
</section>

<section class="about">
  <div class="ph about-photo" role="img" aria-label="Rider on a personal watercraft in front of a waterfront city"></div>
  <div class="about-copy">
    <div class="eyebrow">Tollard Cove Marine</div>
    <h2 class="h-display">About Us</h2>
    <p>Over 50 wet slips, jetski ports and dry storage on two and a half acres of waterfront. We welcome boats from 13 to 50 feet and offer shrink wrapping, bottom painting, detailing, repairs and boat sales, all handled by a friendly, experienced crew.</p>
    <ul class="ticks">
      <li>Your trusted partner in exceptional marine services.</li>
      <li>Boating adventures.</li>
      <li>Expertise to ensure every journey on the water is smooth, safe, and unforgettable.</li>
    </ul>
    <a class="btn btn-outline-dark">Read More</a>
  </div>
</section>

<section class="services">
  <svg class="ph" style="top:-1px;left:0" width="1200" height="120" viewBox="0 0 1200 120"><path d="M0 0 L1200 0 L1200 40 C1000 110 760 20 560 60 C360 100 180 110 0 60Z" fill="#fff"/></svg>
  <div class="sec-head" style="position:absolute;top:150px;width:1200px">
    <div class="eyebrow">Tollard Cove Marine</div>
    <h2 class="h-display">Our Services</h2>
    <p>From floating docks with electric and water to travel lift haul-outs and on-site mechanics, we cover everything your boat needs through every season of the year.</p>
  </div>
  <div class="card-row" style="top:340px">
    <div class="svc">
      <div class="ph svc-photo" style="position:relative;background:linear-gradient(180deg,#7fa7c4,#3d6580)" role="img" aria-label="Boats tied up at floating docks"></div>
      <h3>Dockage</h3>
      <p>Floating docks with dockside electric and water for summer and transient boaters.</p>
      <a class="more">Learn More</a>
    </div>
    <div class="svc">
      <div class="ph svc-photo" style="position:relative;background:linear-gradient(180deg,#5d7ea3,#24415e)" role="img" aria-label="Technician servicing an outboard engine"></div>
      <h3>Mechanical Services</h3>
      <p>Outboard repairs and repowers handled on site by our certified team.</p>
      <a class="more">Learn More</a>
    </div>
    <div class="svc">
      <div class="ph svc-photo" style="position:relative;background:linear-gradient(180deg,#c9955a,#6b4424)" role="img" aria-label="Wood-panelled bathroom inside a boat"></div>
      <h3>Full Bathroom Facilities</h3>
      <p>Member only restrooms and showers kept clean for every guest.</p>
      <a class="more">Learn More</a>
    </div>
  </div>
  <div style="position:absolute;top:688px;width:1200px;text-align:center"><a class="btn btn-outline">View All</a></div>
</section>

<section class="products">
  <svg class="ph" style="top:-1px;left:0" width="1200" height="110" viewBox="0 0 1200 110"><path d="M0 0 L1200 0 L1200 30 C980 100 760 10 540 50 C320 90 160 90 0 40Z" fill="#1b1d1f"/></svg>
  <div class="ph engine" style="left:180px" role="img" aria-label="White outboard motor"></div>
  <div class="ph engine" style="left:860px" role="img" aria-label="White outboard motor"></div>
  <div class="sec-head" style="position:absolute;top:110px;width:1200px">
    <div class="eyebrow" style="color:var(--blue-mid)">Tollard Cove Marine</div>
    <h2 class="h-display">Our Products</h2>
    <p style="width:480px;color:var(--muted)">New and used boat sales plus ferrow and kesta outboards. Browse our current stock and ask our team about repowering the boat you already love.</p>
    <div style="margin-top:18px"><a class="btn btn-outline-dark">View More</a></div>
  </div>
  <div class="ph boat-scene" role="img" aria-label="White motor yacht cruising on the water before a city skyline"></div>
</section>

<section class="blogs">
  <svg class="ph" style="top:-1px;left:0" width="1200" height="60" viewBox="0 0 1200 60"><path d="M0 0 L1200 0 L1200 20 C900 60 400 10 0 40Z" fill="#5d7382" opacity=".35"/></svg>
  <div class="blog-head">
    <div class="eyebrow">Tollard Cove Marine</div>
    <h2 class="h-display">Latest Blogs</h2>
    <p>News, tips and seasonal updates from the dock to help you get the most out of your time on the bay.</p>
  </div>
  <div class="card-row" style="top:190px">
    <div class="post">
      <div class="post-photo" style="background:linear-gradient(180deg,#9ab8cc,#47708c)" role="img" aria-label="Marina with rows of moored boats"></div>
      <h3>Getting Your Boat Ready For Summer</h3>
      <p>A simple checklist to prepare hull, engine and gear before the first launch.</p>
      <a class="more">Read More</a>
    </div>
    <div class="post">
      <div class="post-photo" style="background:linear-gradient(180deg,#7fc0d8,#1f6b8e)" role="img" aria-label="Two riders on personal watercraft"></div>
      <h3>Jetski Safety Tips For The Season</h3>
      <p>Stay safe and have fun with these quick reminders for every rider.</p>
      <a class="more">Read More</a>
    </div>
    <div class="post">
      <div class="post-photo" style="background:linear-gradient(180deg,#8fa7a0,#3e5a55)" role="img" aria-label="Covered slips under a boathouse roof"></div>
      <h3>Choosing Winter Storage Options</h3>
      <p>Wet slip or dry storage? Here is how to pick the right fit for your boat.</p>
      <a class="more">Read More</a>
    </div>
  </div>
</section>

<section class="reviews">
  <svg class="ph" style="top:-1px;left:0" width="1200" height="110" viewBox="0 0 1200 110"><path d="M0 0 L1200 0 L1200 50 C960 110 720 20 480 70 C280 110 140 90 0 60Z" fill="#fff"/></svg>
  <div class="sec-head" style="position:absolute;top:120px;width:1200px">
    <div class="eyebrow">Tollard Cove Marine</div>
    <h2 class="h-display">What Our Clients Says!</h2>
  </div>
  <div class="card-row" style="top:300px">
    <div class="quote">
      <svg width="30" height="24" viewBox="0 0 30 24"><path d="M0 24V12C0 5 4 1 11 0v5c-4 1-5 3-5 7h5v12zM19 24V12c0-7 4-11 11-12v5c-4 1-5 3-5 7h5v12z" fill="#29a8e0"/></svg>
      <p>Friendly staff, clean docks and quick service on my outboard. The best marina we have kept our boat at in years.</p>
      <strong>Dale R.</strong><small>Boat Owner</small>
    </div>
    <div class="quote">
      <svg width="30" height="24" viewBox="0 0 30 24"><path d="M0 24V12C0 5 4 1 11 0v5c-4 1-5 3-5 7h5v12zM19 24V12c0-7 4-11 11-12v5c-4 1-5 3-5 7h5v12z" fill="#29a8e0"/></svg>
      <p>Winter storage was easy and our boat came back ready to run. Great location close to the inlet for fishing.</p>
      <strong>Dale R.</strong><small>Boat Owner</small>
    </div>
    <div class="quote">
      <svg width="30" height="24" viewBox="0 0 30 24"><path d="M0 24V12C0 5 4 1 11 0v5c-4 1-5 3-5 7h5v12zM19 24V12c0-7 4-11 11-12v5c-4 1-5 3-5 7h5v12z" fill="#29a8e0"/></svg>
      <p>Secure gate, good showers and a helpful crew. We stay here every summer and always feel welcome.</p>
      <strong>Dale R.</strong><small>Boat Owner</small>
    </div>
  </div>
</section>
<div class="arrow-btn" style="left:124px"><svg width="12" height="12" viewBox="0 0 12 12"><path d="M8 1 3 6l5 5" fill="none" stroke="#fff" stroke-width="2"/></svg></div>
<div class="arrow-btn" style="left:1040px"><svg width="12" height="12" viewBox="0 0 12 12"><path d="M4 1l5 5-5 5" fill="none" stroke="#fff" stroke-width="2"/></svg></div>

<section class="footer">
  <div class="foot-col" style="left:188px;width:220px">
    <div class="brand brand-dark" style="margin-bottom:18px"><span class="brand-dot"></span>Tollard Cove</div>
    <p style="font-size:12px;line-height:18px;color:var(--muted)">A full-service marina offering dockage, storage, repairs and boat sales in a family friendly setting on the bay.</p>
  </div>
  <div class="foot-col" style="left:440px">
    <h4>Quick Links</h4>
    <ul><li>Services</li><li>Summer Storage</li><li>Winter &amp; Summer Storage</li><li>Transient Dockage</li><li>Mechanical Services</li></ul>
  </div>
  <div class="foot-col" style="left:612px">
    <h4>Contact</h4>
    <ul>
      <li class="row"><svg width="12" height="12" viewBox="0 0 12 12"><path d="M2 1h3l1 3-2 1a7 7 0 003 3l1-2 3 1v3c-6 1-10-3-10-9z" fill="#0677ba"/></svg>(631) 555-0148</li>
      <li class="row"><svg width="12" height="10" viewBox="0 0 12 10"><rect x=".5" y=".5" width="11" height="9" fill="none" stroke="#0677ba"/><path d="M.5.5 6 5l5.5-4.5" fill="none" stroke="#0677ba"/></svg>hello@tollardcove.com</li>
      <li class="row" style="align-items:flex-start"><svg width="12" height="14" viewBox="0 0 12 14" style="margin-top:5px"><path d="M6 14S1 8 1 5a5 5 0 0110 0c0 3-5 9-5 9z" fill="#0677ba"/><circle cx="6" cy="5" r="2" fill="#fff"/></svg><span style="line-height:17px;padding-top:3px">12 Harbor Lane,<br>Tollard Cove</span></li>
    </ul>
  </div>
  <div class="connect">
    <h4>Let's Connect!</h4>
    <div class="field">Your Name</div>
    <div class="field">Email Address</div>
    <div class="field">Phone Number</div>
    <div class="submit">SUBMIT</div>
  </div>
</section>
<div class="copyright">Copyright 2024 Tollard Cove Marine. All Rights Reserved</div>

</body>
</html>
```